Der Designer hat mir ein super Logo entworfen sehr schnell tolle Zusammenarbeit. Ist nur zu empfehlen
Zielgruppe
Es handelt sich um eine Haus und Immobilienverwaltung die Zielgruppe sind Eigentümer der Häuser und Firmen
Aufgabenstellung
Edel klassisch

```html
<!DOCTYPE html>
<html lang="de">
<head>
<meta charset="utf-8">
<title>Varholt Unternehmensgruppe – Geschäftsausstattung</title>
<link rel="stylesheet" href="https://fonts.googleapis.com/css2?family=Roboto:wght@300;400&display=swap">
<style>
  :root {
    --stage: #4b4b4b;
    --card-dark: #363636;
    --card-light: #ffffff;
    --blue: #78afc9;
    --green: #86a898;
    --grey-text: #555555;
    --grey-name: #7d7d78;
    --grey-mark: #b3b3b3;
    --band-grey: #b6b6b6;
  }
  * { margin: 0; padding: 0; box-sizing: border-box; }
  html, body { width: 1200px; height: 1200px; overflow: hidden; }
  body {
    background: var(--stage);
    font-family: "Roboto", Arial, sans-serif;
    font-weight: 300;
    position: relative;
  }
  .card {
    position: absolute;
    width: 467px;
    height: 302px;
    box-shadow: 5px 5px 8px rgba(0,0,0,.35);
    overflow: hidden;
  }
  .card--front { left: 366px; top: 257px; background: var(--card-dark); }
  .card--back-a { left: 75px; top: 609px; background: var(--card-light); }
  .card--back-b { left: 663px; top: 609px; background: var(--card-light); }

  .abs { position: absolute; white-space: nowrap; }

  /* Brand block */
  .brand { position: absolute; text-align: center; color: var(--grey-mark); }
  .brand__square { background: var(--blue); margin: 0 auto; }
  .brand__name { font-weight: 400; line-height: 1; }
  .brand__sub { font-weight: 400; line-height: 1; }

  .card--front .brand { left: 101px; top: 48px; width: 267px; }
  .card--front .brand__square { width: 92px; height: 92px; margin-bottom: 22px; }
  .card--front .brand__name { font-size: 34px; letter-spacing: 11px; margin-right: -11px; }
  .card--front .brand__sub { font-size: 13.5px; letter-spacing: 2.6px; margin-top: 8px; }

  .card--back-a .brand { left: 286px; top: 25px; width: 150px; }
  .card--back-b .brand { left: 27px; top: 81px; width: 150px; }
  .card--back-a .brand__square,
  .card--back-b .brand__square { width: 54px; height: 54px; margin-bottom: 12px; }
  .card--back-a .brand__name,
  .card--back-b .brand__name { font-size: 20px; letter-spacing: 6px; margin-right: -6px; }
  .card--back-a .brand__sub,
  .card--back-b .brand__sub { font-size: 7.4px; letter-spacing: 1.3px; margin-top: 4px; }

  /* Contact text */
  .address, .contact { font-size: 12.5px; color: var(--grey-text); line-height: 19px; }
  .contact__heading { color: var(--green); font-size: 13.5px; margin-bottom: 3px; }
  .contact__row { line-height: 21.3px; }
  .contact__label { color: var(--blue); margin-right: 3px; }

  .person { text-align: center; }
  .person__name { font-size: 21px; color: var(--grey-name); font-weight: 400; line-height: 1.1; }
  .person__role { font-size: 11.5px; color: var(--grey-text); margin-top: 4px; }

  .accent-bar { position: absolute; left: 0; top: 158px; width: 27px; height: 58px; background: var(--green); }

  .band { position: absolute; left: 0; top: 263px; width: 467px; height: 11px; display: flex; }
  .band__grey { width: 100px; background: var(--band-grey); }
  .band__green { flex: 1; background: var(--green); }
</style>
</head>
<body>

  <section class="card card--front" aria-label="Vorderseite">
    <div class="brand">
      <div class="brand__square"></div>
      <div class="brand__name">VARHOLT</div>
      <div class="brand__sub">UNTERNEHMENSGRUPPE GmbH</div>
    </div>
  </section>

  <section class="card card--back-a" aria-label="Rückseite Variante A">
    <div class="address abs" style="left:41px; top:83px;">
      Lindenhofweg 12<br>10827 Berlin
    </div>
    <div class="accent-bar"></div>
    <div class="contact abs" style="left:41px; top:134px;">
      <div class="contact__heading">Kontakt</div>
      <div class="contact__row"><span class="contact__label">Telefon:</span> +49 030 555 02 718</div>
      <div class="contact__row"><span class="contact__label">Telefax:</span> +49 030 555 02 718</div>
      <div class="contact__row"><span class="contact__label">E-Mail:</span> Varholt@Varholt GmbH.de</div>
    </div>
    <div class="brand">
      <div class="brand__square"></div>
      <div class="brand__name">VARHOLT</div>
      <div class="brand__sub">UNTERNEHMENSGRUPPE GmbH</div>
    </div>
    <div class="person abs" style="left:284px; top:172px; width:150px;">
      <div class="person__name">Lena Varholt</div>
      <div class="person__role">Geschäftsführer</div>
    </div>
    <div class="band"><div class="band__grey"></div><div class="band__green"></div></div>
  </section>

  <section class="card card--back-b" aria-label="Rückseite Variante B">
    <div class="person abs" style="left:225px; top:24px; width:150px;">
      <div class="person__name">Lena Varholt</div>
      <div class="person__role">Geschäftsführer</div>
    </div>
    <div class="brand">
      <div class="brand__square"></div>
      <div class="brand__name">VARHOLT</div>
      <div class="brand__sub">UNTERNEHMENSGRUPPE GmbH</div>
    </div>
    <div class="address abs" style="left:235px; top:100px;">
      Lindenhofweg 12<br>10827 Berlin
    </div>
    <div class="contact abs" style="left:235px; top:151px;">
      <div class="contact__heading">Kontakt</div>
      <div class="contact__row"><span class="contact__label">Telefon:</span> +49 030 555 02 718</div>
      <div class="contact__row"><span class="contact__label">Telefax:</span> +49 030 555 02 718</div>
      <div class="contact__row"><span class="contact__label">E-Mail:</span> Varholt@Varholt GmbH.de</div>
    </div>
    <div class="band"><div class="band__grey"></div><div class="band__green"></div></div>
  </section>

</body>
</html>
```